Full Page Color Ad

We need a full page 8.5 x 11 ad created for a magazine. Please see the attached examples. It would be best if the wording/style stayed the same. As far as background image, we are looking for something catchy that portrays "hidden treasure". Please be sure to include the logos as well. If you have any questions or need anything else, please email rmoreno@ridgewave.com You can also visit www.ridgewave.com to learn at little about our company and see our branding/style.
*Please follow the style and wording of the examples as best as possible. Not looking for variation on the text layout- more ofthe background and added creativity.*
It Company

```html
<!DOCTYPE html>
<html lang="en">
<head>
<meta charset="utf-8">
<title>Discover Hidden Value – Ridgewave</title>
<link rel="stylesheet" href="https://fonts.googleapis.com/css2?family=Archivo:wght@400;700&family=Oswald:wght@600&display=swap">
<style>
  :root {
    --page-bg: #e9e6e1;
    --gold: #f0b31a;
    --orange: #ef7f1a;
    --navy: #142a45;
    --ink: #1b2a3a;
    --white: #ffffff;
    --sea-top: #0a93d8;
    --sea-mid: #0a62c0;
    --sea-deep: #073a8c;
    --sea-floor: #03205a;
    --shoal-light: rgba(150, 205, 240, 0.75);
    --shoal-mid: rgba(90, 160, 215, 0.6);
    --shoal-fin: rgba(170, 190, 80, 0.35);
    --brand-blue: #0b4a9a;
  }
  * { margin: 0; padding: 0; box-sizing: border-box; }
  html, body {
    width: 900px; height: 1200px; overflow: hidden;
    background: var(--page-bg);
  }
  .ad {
    position: absolute; left: 10px; top: 30px;
    width: 881px; height: 1140px; overflow: hidden;
    font-family: "Archivo", Arial, sans-serif;
  }
  .ad__sea {
    position: absolute; inset: 0;
    background: linear-gradient(180deg, var(--sea-top) 0%, var(--sea-mid) 30%, var(--sea-deep) 60%, var(--sea-floor) 100%);
  }
  .ad__shoal {
    position: absolute; left: 0; right: 0; top: 560px; height: 500px;
    background:
      radial-gradient(ellipse 30% 18% at 55% 30%, var(--shoal-light), transparent 70%),
      radial-gradient(ellipse 28% 16% at 78% 48%, var(--shoal-light), transparent 70%),
      radial-gradient(ellipse 26% 14% at 22% 70%, var(--shoal-light), transparent 70%),
      radial-gradient(ellipse 35% 20% at 40% 52%, var(--shoal-mid), transparent 75%),
      radial-gradient(ellipse 30% 20% at 85% 20%, var(--shoal-mid), transparent 75%),
      radial-gradient(ellipse 40% 25% at 15% 25%, var(--shoal-mid), transparent 75%),
      radial-gradient(ellipse 60% 40% at 50% 50%, var(--shoal-fin), transparent 80%);
  }
  .headline-band {
    position: absolute; left: 20px; top: 95px; right: 0; height: 97px;
    background: var(--gold);
  }
  .headline {
    position: absolute; left: 39px; top: 14px;
    font-size: 71px; font-weight: 400; color: var(--ink);
    letter-spacing: -0.5px; line-height: 1; white-space: nowrap;
  }
  .headline strong { font-weight: 700; }
  .band-fold { position: absolute; left: 0; top: 135px; }
  .lead {
    position: absolute; left: 101px; top: 254px;
    font-size: 47px; font-weight: 700; color: var(--gold); line-height: 1;
  }
  .process-list {
    position: absolute; left: 380px; top: 258px; list-style: none;
    font-family: "Oswald", "Arial Narrow", sans-serif; font-weight: 600;
    font-size: 24px; line-height: 31px; color: var(--white);
    text-transform: uppercase; letter-spacing: 0.2px;
  }
  .process-list .is-active { color: var(--gold); }
  .tail {
    position: absolute; left: 604px; top: 370px;
    font-size: 50px; font-weight: 700; color: var(--gold); line-height: 1;
  }
  .brand-mark {
    position: absolute; left: 51px; top: 1016px; width: 80px; height: 80px;
    background: var(--brand-blue);
    padding: 8px 5px; color: var(--white);
    font-size: 14px; font-weight: 700; line-height: 1;
  }
  .blurb {
    position: absolute; left: 158px; top: 1024px; width: 530px;
    font-size: 12px; line-height: 16.4px; color: var(--white);
    white-space: nowrap;
  }
  .partner-badge { position: absolute; left: 694px; top: 1018px; }
  .footer-bar {
    position: absolute; left: 0; right: 0; top: 1118px; height: 22px;
    background: var(--gold);
  }
</style>
</head>
<body>
  <main class="ad">
    <div class="ad__sea" role="img" aria-label="Underwater photograph of a school of silver fish swimming over a reef in deep blue water">
      <div class="ad__shoal"></div>
    </div>

    <svg class="band-fold" width="105" height="97" viewBox="0 0 105 97" aria-hidden="true">
      <rect x="0" y="0" width="20" height="97" fill="var(--orange)"/>
      <polygon points="20,57 105,57 105,97 20,97" fill="var(--orange)"/>
      <polygon points="20,57 105,57 105,97" fill="var(--navy)" opacity="0.85"/>
    </svg>

    <div class="headline-band">
      <h1 class="headline">Discover <strong>Hidden</strong> Value</h1>
    </div>

    <p class="lead">From Your</p>
    <ul class="process-list">
      <li>Consolidations</li>
      <li>Financial Planning</li>
      <li>Strategy Management</li>
      <li>Profitability</li>
      <li class="is-active">Performance<br>Management</li>
      <li>Balanced Scorecard</li>
      <li>Sales &amp; Operations<br>Planning</li>
    </ul>
    <p class="tail">Process.</p>

    <div class="brand-mark">ridgewave</div>
    <p class="blurb">Ridgewave is trusted by more companies globally to deliver high value solutions featuring<br>Veltrix’s Business Analytics portfolio. Our team offers visionary services that maximize the<br>business value your company can realize from these powerful products. Contact us<br>today for more information.</p>

    <svg class="partner-badge" width="136" height="79" viewBox="0 0 136 79" aria-hidden="true">
      <rect x="0" y="0" width="136" height="79" fill="var(--brand-blue)"/>
    </svg>

    <div class="footer-bar"></div>
  </main>
</body>
</html>
```